Business Card Design Project

Design is for the business card of a holistic, integral therapist. Design is required for front (colour / pattern) and back (white, with text as below).

Please prepare the design using placeholder text. I will work with the winning submission to complete the final information in the last iteration.

To give you a sense of her services a profile is below:
- I offer an integrative approach for effective relief of many issues such as anxiety, panic attacks, relationship difficulties, and health problems. In my counselling sessions I mainly use EFT {Emotional Freedom Technique } which taps into the body's energy system (meridians) to clear up blockages and limiting /distorted thinking and beliefs. I also work on expanding awareness as well as enhancing relationships.Clients have found the sessions life changing and report feeling lighter, clearer more empowered and connected to themselves and others.

Target Market(s)

Well educated, upper socioeconomic people seeking purpose and happiness in their lives.

Industry/Entity Type

Health

Requirements
Must have
• Must have the following text on front

First Name, Last Name
LLB, ND, Dip C
Counselling & Naturopathy
Emotional Feedom Technique and Bowen Therapy

Adress 1 Line 1
Adress 1 Line 2

Adress 2 Line 1
Adress 2 Line 2

xxx.xxx@xxxxx.com

Tel: 0XXX XXX XXX

Must have the following text on reverse - which should be primarily white.

Next appointment
Date:
Time:
Nice to have
• Example colour palettes

http://www.huepinwheel.net/palette/512093/velvet_lantern
http://www.huepinwheel.net/palette/308215/Quiet_Orchard
http://www.huepinwheel.net/palette/426958/Soft_Harbor_Glow

Example images that may be useful...
http://www.brindlemart.net/gp/product/images/4719260351/ref=dp_image_text_0?ie=UTF8&n=617204&s=books
http://www.brindlemart.net/gp/customer-media/product-gallery/5280147936/ref=cm_ciu_pdp_images_all
http://en.lorewell.org/wiki/File:Lotus_Grid_256bw.gif

```html
<!DOCTYPE html>
<html lang="en">
<head>
<meta charset="utf-8">
<title>Therapist Business Card – Front and Reverse</title>
<link rel="stylesheet" href="https://fonts.googleapis.com/css2?family=Source+Sans+3:wght@400;600;700&family=Reenie+Beanie&display=swap">
<style>
  :root {
    --stage: #3b3b3b;
    --paper: #ffffff;
    --ink-dark: #2b2418;
    --ink-body: #5a4a32;
    --accent-orange: #d98a2b;
    --sage: #9bb0a8;
    --sage-box: #a9bdb5;
    --sage-text: #8ea69d;
    --rule-tan: #c9a57a;
    --label-tan: #b9874f;
    --leaf-pale: #e6ebd2;
    --leaf-green: #c9d3a6;
    --leaf-olive: #8e9658;
    --leaf-amber: #e0a262;
    --leaf-rust: #b9652d;
    --yantra-mist: #eef2f0;
    --yantra-line: #d9e2de;
  }

  * { box-sizing: border-box; margin: 0; padding: 0; }

  html, body {
    width: 1200px;
    height: 943px;
    overflow: hidden;
    background: var(--stage);
    font-family: "Source Sans 3", Arial, sans-serif;
  }

  .canvas {
    position: relative;
    width: 1200px;
    height: 943px;
  }

  .card {
    position: absolute;
    width: 712px;
    height: 426px;
    overflow: hidden;
  }

  /* ---------- Front ---------- */
  .card--front { left: 45px; top: 60px; }

  .front-artwork {
    position: absolute;
    inset: 0;
    background:
      radial-gradient(ellipse 60% 45% at 62% 62%, rgba(224,162,98,0.85), rgba(224,162,98,0) 70%),
      radial-gradient(ellipse 45% 30% at 72% 18%, rgba(201,120,60,0.75), rgba(201,120,60,0) 70%),
      radial-gradient(ellipse 55% 40% at 85% 85%, rgba(185,101,45,0.8), rgba(185,101,45,0) 70%),
      linear-gradient(120deg, var(--leaf-pale) 0%, var(--leaf-green) 45%, var(--leaf-olive) 100%);
  }

  .front-details {
    position: absolute;
    left: 50px;
    top: 72px;
    color: var(--ink-body);
  }

  .practitioner-name {
    font-size: 20px;
    font-weight: 700;
    color: var(--ink-dark);
    line-height: 24px;
  }

  .credentials,
  .services {
    font-size: 19px;
    font-weight: 400;
    color: var(--accent-orange);
    line-height: 24px;
  }

  .contact {
    margin-top: 16px;
    font-size: 14px;
    line-height: 19px;
    font-style: normal;
  }

  .contact p + p { margin-top: 18px; }

  /* ---------- Reverse ---------- */
  .card--back {
    left: 401px;
    top: 451px;
    background: var(--paper);
  }

  .appointment-title {
    position: absolute;
    left: 63px;
    top: 88px;
    font-size: 20px;
    font-weight: 700;
    letter-spacing: 0.3px;
    color: var(--sage-text);
  }

  .weekdays {
    position: absolute;
    left: 63px;
    top: 121px;
    display: flex;
    gap: 8px;
    list-style: none;
  }

  .weekday {
    width: 38px;
    display: flex;
    flex-direction: column;
    align-items: center;
    font-size: 15px;
    font-weight: 600;
    color: var(--sage-text);
  }

  .weekday--wide { width: 44px; }

  .weekday-box {
    margin-top: 4px;
    width: 38px;
    height: 38px;
    background: var(--sage-box);
    display: flex;
    align-items: center;
    justify-content: center;
  }

  .weekday--wide .weekday-box { width: 38px; }

  .field {
    position: absolute;
    left: 63px;
    display: flex;
    align-items: flex-end;
    font-size: 15px;
    color: var(--label-tan);
  }

  .field-line {
    display: block;
    border-bottom: 1px solid var(--rule-tan);
    height: 1px;
    margin-left: 2px;
    margin-bottom: 3px;
  }

  .field--date { top: 220px; }
  .field--date .field-line { width: 363px; }
  .field--time { top: 276px; }
  .field--time .field-line { width: 214px; }

  .thank-you {
    position: absolute;
    left: 63px;
    top: 334px;
    font-family: "Reenie Beanie", cursive;
    font-size: 30px;
    color: var(--sage);
  }

  .yantra-mark {
    position: absolute;
    left: 408px;
    top: 93px;
    width: 244px;
    height: 244px;
    background: radial-gradient(circle at 50% 50%, var(--yantra-line) 0%, var(--yantra-mist) 60%, var(--paper) 100%);
  }
</style>
</head>
<body>
<main class="canvas">

  <section class="card card--front" aria-label="Business card front">
    <div class="front-artwork" role="img" aria-label="Backlit autumn leaf photograph in amber and olive tones overlaid with a white line yantra ornament"></div>
    <div class="front-details">
      <h1 class="practitioner-name">First Name, Last Name</h1>
      <p class="credentials">LLB, ND, Dip C</p>
      <p class="services">Counselling &amp; Naturopathy</p>
      <p class="services">Emotional Feedom Technique &amp; Bowen Therapy</p>
      <address class="contact">
        <p>Adress 1 Line 1<br>Adress 1 Line 2</p>
        <p>Adress 2 Line 1<br>Adress 2 Line 2</p>
        <p>xxx.xxx@xxxxx.com</p>
        <p>Tel: 0XXX XXX XXX</p>
      </address>
    </div>
  </section>

  <section class="card card--back" aria-label="Business card reverse">
    <h2 class="appointment-title">NEXT APPOINTMENT</h2>
    <ul class="weekdays">
      <li class="weekday">MON<span class="weekday-box"></span></li>
      <li class="weekday">TUES<span class="weekday-box">
        <svg width="28" height="28" viewBox="0 0 28 28" aria-label="Selected">
          <path d="M4 15 L11 22 L25 5" fill="none" stroke="#1a1a1a" stroke-width="4" stroke-linecap="round" stroke-linejoin="round"/>
        </svg>
      </span></li>
      <li class="weekday">WED<span class="weekday-box"></span></li>
      <li class="weekday weekday--wide">THURS<span class="weekday-box"></span></li>
      <li class="weekday">FRI<span class="weekday-box"></span></li>
    </ul>
    <p class="field field--date">Date:<span class="field-line"></span></p>
    <p class="field field--time">Time:<span class="field-line"></span></p>
    <p class="thank-you">Thank you.</p>
    <div class="yantra-mark" role="img" aria-label="Faint sage line yantra ornament"></div>
  </section>

</main>
</body>
</html>
```